Most captivating card ever!

Life Coach - Professional Adventurer - Entrepreneur
I need the worlds most amazing business card for my personal brand. This business card will mostly be used to give to prospective clients for life coaching and business coaching.
Be creative, be adventurous. It needs to stand out. Make people say.. I need this guy!
My background is as an entrepreneur and professional adventurer undertaking extreme expeditions. I am now moving into life coaching.
No specific design ideas, so you have full creativity. Show me your best.
Industry/Entity Type
Life Coaching
Contact Information for Business Card
Dan Pellow
itsdanp.com.au
0468215903
Colors
Designer to choose colors to be used in the design.
Look and feel

```html
<!DOCTYPE html>
<html lang="en">
<head>
<meta charset="utf-8">
<title>Dan Pellow – Business Card</title>
<link rel="stylesheet" href="https://fonts.googleapis.com/css2?family=Anton&family=Oswald:wght@400;500&display=swap">
<style>
  :root {
    --backdrop: #ececec;
    --card-teal: #82cfcf;
    --card-ink: #ffffff;
  }
  html, body {
    margin: 0;
    padding: 0;
    width: 1200px;
    height: 1000px;
    overflow: hidden;
    background: var(--backdrop);
  }
  .canvas {
    position: relative;
    width: 1200px;
    height: 1000px;
  }
  .business-card {
    position: absolute;
    left: 210px;
    top: 278px;
    width: 780px;
    height: 444px;
    border-radius: 30px;
    background: var(--card-teal);
    color: var(--card-ink);
    text-align: center;
  }
  .card-line {
    position: absolute;
    left: 0;
    right: 0;
    margin: 0;
    line-height: 1;
  }
  .holder-name {
    top: 80px;
    font-family: "Anton", "Oswald", sans-serif;
    font-size: 36px;
    letter-spacing: 2.5px;
    font-weight: 400;
  }
  .holder-roles {
    top: 149px;
    font-family: "Oswald", sans-serif;
    font-weight: 400;
    font-size: 19px;
    letter-spacing: 1.6px;
  }
  .divider {
    position: absolute;
    top: 208px;
    left: 343px;
    width: 114px;
    height: 3px;
    background: var(--card-ink);
  }
  .holder-phone,
  .holder-site {
    font-family: "Oswald", sans-serif;
    font-weight: 500;
    font-size: 25px;
    letter-spacing: 2.5px;
  }
  .holder-phone { top: 253px; }
  .holder-site { top: 314px; }
</style>
</head>
<body>
  <main class="canvas">
    <section class="business-card" aria-label="Business card for Dan Pellow">
      <h1 class="card-line holder-name">DAN PELLOW</h1>
      <p class="card-line holder-roles">LIFE COACH - PROFESSIONAL ADVENTURER - ENTREPRENEUR</p>
      <div class="divider"></div>
      <p class="card-line holder-phone">0468215903</p>
      <p class="card-line holder-site">ITSDANP.COM.AU</p>
    </section>
  </main>
</body>
</html>
```